Design a BOLD Ad Design for Fitness Club

We are fitness facility that is about to run our new "Sunrise Mama Reset" program and we need a bold design created for an ad that will run on Instagram and Facebook.

The ad needs to be eye catching, easy to read and attractive so that someone stops scrolling and clicks to join.

The add needs to be sized to 1080 x 1080, include our logo and the text "Sunrise Mama Reset" and "Starting September 23rd"

I have included an example photo, which is to be used as an example only of a design style that stands out to us, (colors, female photo style, etc)

I have also included our logo, which the yellow color can be changed for this design.

Thank you and we look forward to seeing your design.

```html
<!DOCTYPE html>
<html lang="en">
<head>
<meta charset="UTF-8">
<title>PulseForge – Sunrise Mama Reset</title>
<link rel="stylesheet" href="https://fonts.googleapis.com/css2?family=Kanit:ital,wght@0,700;1,800;1,900&family=Bebas+Neue&family=Poppins:wght@400;500&display=swap">
<style>
  :root {
    --ink: #0c0a0b;
    --charcoal: #2a2628;
    --magenta: #b8136f;
    --magenta-deep: #7e0c4c;
    --skin: #c98a72;
    --white: #ffffff;
    --url-ink: #1d1a1c;
  }
  * { margin: 0; padding: 0; box-sizing: border-box; }
  html, body { width: 1200px; height: 1200px; overflow: hidden; background: var(--ink); }
  .ad {
    position: relative; width: 1200px; height: 1200px; overflow: hidden;
    background: radial-gradient(ellipse at 45% 55%, var(--charcoal) 0%, var(--ink) 62%);
    font-family: "Kanit", sans-serif; color: var(--white);
  }
  .accent-field {
    position: absolute; right: 0; top: 0; width: 360px; height: 1060px;
    background: linear-gradient(100deg, rgba(184,19,111,0) 0%, var(--magenta) 40%, var(--magenta) 100%);
  }
  .hero-photo {
    position: absolute; left: 770px; top: 150px; width: 430px; height: 920px;
    background: radial-gradient(ellipse at 45% 40%, var(--skin) 0%, #9a5d4c 38%, var(--magenta) 66%, var(--magenta-deep) 100%);
    border-radius: 48% 0 0 0 / 16% 0 0 0;
    opacity: .94;
  }
  .brand { position: absolute; left: 97px; top: 112px; width: 392px; text-align: center; }
  .brand-name { font-size: 88px; font-weight: 700; line-height: 1; letter-spacing: -1px; }
  .brand-tag { margin-top: 14px; font-size: 15px; font-weight: 700; letter-spacing: 2.5px; }
  .headline { position: absolute; left: 84px; top: 372px; font-style: italic; font-weight: 900; text-transform: uppercase; line-height: 1; }
  .headline span { display: block; }
  .line-one { font-size: 112px; margin-left: 18px; }
  .line-two { font-size: 160px; color: var(--magenta); margin-top: -16px; letter-spacing: -2px; }
  .line-three { font-size: 112px; margin-top: -10px; }
  .starting { position: absolute; left: 119px; top: 782px; font-family: "Poppins", sans-serif; font-size: 34px; letter-spacing: 13px; font-weight: 400; }
  .dot-grid { position: absolute; }
  .dot-grid.upper { left: 454px; top: 785px; }
  .dot-grid.lower { left: 3px; top: 972px; }
  .date-badge { position: absolute; left: 92px; top: 840px; width: 190px; height: 130px; border-radius: 50%; background: var(--white); }
  .date-day {
    position: absolute; left: 100px; top: 834px; font-size: 134px; font-style: italic; font-weight: 900;
    color: var(--magenta); line-height: 1; letter-spacing: -6px;
  }
  .date-suffix { position: absolute; left: 294px; top: 846px; font-size: 40px; font-style: italic; font-weight: 900; line-height: 1; }
  .date-month { position: absolute; left: 288px; top: 892px; font-family: "Bebas Neue", sans-serif; font-size: 90px; line-height: 1; letter-spacing: -1px; }
  .footer-band { position: absolute; left: 0; bottom: 0; width: 1200px; height: 170px; }
  .site-url {
    position: absolute; left: 97px; top: 1094px; font-family: "Poppins", sans-serif;
    font-size: 40px; letter-spacing: 6px; color: var(--url-ink);
  }
</style>
</head>
<body>
<main class="ad">
  <div class="accent-field"></div>
  <div class="hero-photo" role="img" aria-label="Photo of a fit woman in a magenta sports top lifting a dumbbell overhead"></div>

  <div class="brand">
    <div class="brand-name">PulseForge</div>
    <div class="brand-tag">PERSONAL GROUP TRAINING</div>
  </div>

  <h1 class="headline">
    <span class="line-one">Sunrise</span>
    <span class="line-two">Mama</span>
    <span class="line-three">Reset</span>
  </h1>

  <div class="starting">STARTING</div>
  <svg class="dot-grid upper" width="142" height="36" viewBox="0 0 142 36" aria-hidden="true">
    <defs><pattern id="dotsA" width="12" height="12" patternUnits="userSpaceOnUse"><circle cx="4" cy="4" r="3" fill="#8a8688"/></pattern></defs>
    <rect width="142" height="36" fill="url(#dotsA)"/>
  </svg>
  <svg class="dot-grid lower" width="64" height="36" viewBox="0 0 64 36" aria-hidden="true">
    <defs><pattern id="dotsB" width="12" height="12" patternUnits="userSpaceOnUse"><circle cx="4" cy="4" r="3" fill="#8a8688"/></pattern></defs>
    <rect width="64" height="36" fill="url(#dotsB)"/>
  </svg>

  <div class="date-badge"></div>
  <div class="date-day">23</div>
  <div class="date-suffix">RD</div>
  <div class="date-month">SEPTEMBER</div>

  <svg class="footer-band" viewBox="0 0 1200 170" preserveAspectRatio="none" aria-hidden="true">
    <path fill="#ffffff" d="M0 30 L40 22 L90 34 L150 20 L210 30 L260 14 L320 26 L380 10 L430 22 L470 4 L520 18 L580 8 L640 24 L700 12 L760 26 L820 16 L880 30 L930 18 L990 34 L1050 22 L1110 36 L1160 24 L1200 30 L1200 170 L0 170 Z"/>
  </svg>
  <div class="site-url">www.pulseforgefit.com</div>
</main>
</body>
</html>
```